Double Sided Flyer for 3D printing services company

We need a nice balanced flyer for our corporate handout. The attached is for concept only and not the final design. We think the attached examples have elements that balance nicely but the graphics are not good. We are attaching the logo from the corporate office for our new logo. We will add the company information after the final design is selected for web address, phone, mailing etc. Please leave room for that information in the design. Please ask any questions prior to submission. Our main focus is printing RUBBER 3D Parts and not plastic parts. The images selected should be focused on that. We also need to ensure the images are approved for use in a corporate flyer for content.

```html
<!DOCTYPE html>
<html lang="en">
<head>
<meta charset="utf-8">
<title>Corvane – Rubber 3D Printing Flyer</title>
<link rel="stylesheet" href="https://fonts.googleapis.com/css2?family=Poppins:ital,wght@0,400;0,600;0,700;1,300&display=swap">
<style>
  :root {
    --orange: #e0562a;
    --slate: #59595b;
    --ink: #4a4a4c;
    --backdrop: #dedee0;
    --paper: #ffffff;
    --photo-steel: #9aa0a8;
    --photo-blue: #2f73c9;
    --photo-office: #b9bcbc;
  }
  * { box-sizing: border-box; margin: 0; padding: 0; }
  html, body { width: 1200px; height: 1157px; overflow: hidden; }
  body {
    background: var(--backdrop);
    font-family: "Poppins", sans-serif;
    position: relative;
  }
  .page {
    position: absolute;
    width: 551px;
    height: 714px;
    background: var(--paper);
    overflow: hidden;
  }
  .page--front { left: 32px; top: 90px; }
  .page--back { left: 616px; top: 312px; }
  .shape { position: absolute; inset: 0; width: 551px; height: 714px; }

  .brand {
    position: absolute;
    display: flex;
    align-items: center;
    gap: 8px;
  }
  .brand__dot {
    border-radius: 50%;
    background: var(--orange);
    flex: none;
  }
  .brand__text { display: flex; flex-direction: column; }
  .brand__name {
    font-weight: 700;
    color: var(--ink);
    line-height: 1;
    letter-spacing: 0.5px;
  }
  .brand__tagline {
    font-weight: 600;
    color: var(--ink);
    letter-spacing: 1.2px;
    line-height: 1.2;
  }
  .page--front .brand { left: 290px; top: 40px; }
  .page--front .brand__dot { width: 48px; height: 48px; }
  .page--front .brand__name { font-size: 37px; }
  .page--front .brand__tagline { font-size: 10.5px; margin-top: 3px; }
  .page--back .brand { left: 368px; top: 48px; }
  .page--back .brand__dot { width: 32px; height: 32px; }
  .page--back .brand__name { font-size: 25px; }
  .page--back .brand__tagline { font-size: 7.2px; margin-top: 2px; }

  .product-photo {
    position: absolute;
    left: 21px; top: 36px;
    width: 235px; height: 214px;
    background: radial-gradient(ellipse at 50% 45%, #5a5a5c 0%, #3a3a3c 30%, #e4e5e8 62%, #f3f3f5 100%);
  }

  .highlights {
    position: absolute;
    left: 78px; top: 399px;
    width: 317px; height: 279px;
    background: var(--orange);
    border-radius: 11px;
    padding: 22px 14px 0 16px;
    color: var(--paper);
  }
  .highlights__title {
    font-weight: 300;
    font-style: italic;
    font-size: 25.5px;
    line-height: 1.2;
    margin-bottom: 18px;
  }
  .highlights__list { list-style: none; }
  .highlights__item {
    font-weight: 700;
    font-size: 15.6px;
    line-height: 1.2;
    margin-bottom: 18px;
  }

  .intro {
    position: absolute;
    left: 28px;
    font-weight: 700;
    font-size: 16px;
    line-height: 1.18;
  }
  .intro--top { top: 46px; color: var(--orange); }
  .intro--panel { top: 309px; color: var(--paper); }

  .feature {
    position: absolute;
    width: 140px;
    color: var(--paper);
  }
  .feature__icon { width: 22px; height: 22px; display: block; margin-bottom: 8px; }
  .feature__title {
    font-weight: 700;
    font-size: 10.4px;
    line-height: 1.25;
    text-transform: uppercase;
    margin-bottom: 9px;
  }
  .feature__body {
    font-weight: 400;
    font-size: 9.3px;
    line-height: 1.16;
  }
  .feature--a { left: 31px; top: 362px; }
  .feature--b { left: 212px; top: 362px; }
  .feature--c { left: 393px; top: 362px; }
  .feature--d { left: 31px; top: 526px; }
  .feature--e { left: 212px; top: 526px; }

  .contact-bar {
    position: absolute;
    left: 0; top: 680px;
    width: 551px; height: 34px;
    background: var(--orange);
    color: var(--paper);
    font-weight: 600;
    font-size: 10px;
  }
  .contact-bar span { position: absolute; top: 10px; }
  .contact-bar .phone { left: 31px; }
  .contact-bar .web { left: 212px; }
  .contact-bar .mail { left: 396px; }
</style>
</head>
<body>

<section class="page page--front">
  <svg class="shape" viewBox="0 0 551 714" aria-hidden="true">
    <defs>
      <linearGradient id="printerTones" x1="0" y1="0" x2="1" y2="1">
        <stop offset="0" stop-color="#8a5bb0"/>
        <stop offset="0.45" stop-color="var(--photo-blue)"/>
        <stop offset="1" stop-color="#1f5fb0"/>
      </linearGradient>
    </defs>
    <polygon points="0,0 119,0 0,61" fill="var(--orange)"/>
    <polygon points="0,398 551,127 551,577 474,653 0,653" fill="url(#printerTones)"
             role="img" aria-label="Photo of a 3D printer print head printing a rubber part"/>
    <polygon points="444,714 551,611 551,714" fill="var(--slate)"/>
  </svg>

  <div class="product-photo" role="img" aria-label="Photo of assorted black moulded rubber plugs and seals"></div>

  <div class="brand">
    <span class="brand__dot"></span>
    <span class="brand__text">
      <span class="brand__name">CORVANE</span>
      <span class="brand__tagline">SEALS·GASKETS·HOSES</span>
    </span>
  </div>

  <div class="highlights">
    <h1 class="highlights__title">RUBBER SEALS GASKETS<br>HOSES 3D PRINTING</h1>
    <ul class="highlights__list">
      <li class="highlights__item">Reduce time to market from<br>weeks to hours</li>
      <li class="highlights__item">Eliminate costly design errors</li>
      <li class="highlights__item">faster time to market</li>
      <li class="highlights__item">Reduce R&amp;D Budget</li>
    </ul>
  </div>
</section>

<section class="page page--back">
  <svg class="shape" viewBox="0 0 551 714" aria-hidden="true">
    <defs>
      <linearGradient id="officeTones" x1="0" y1="0" x2="1" y2="0">
        <stop offset="0" stop-color="#c9c6bd"/>
        <stop offset="0.5" stop-color="#e6e8e8"/>
        <stop offset="1" stop-color="#6f7a80"/>
      </linearGradient>
    </defs>
    <polygon points="492,0 551,0 551,54" fill="var(--orange)"/>
    <rect x="0" y="98" width="543" height="310" fill="url(#officeTones)"
          role="img" aria-label="Photo of engineers reviewing a part design on a computer screen"/>
    <polygon points="0,266 210,266 551,407 551,680 0,680" fill="var(--slate)"/>
    <line x1="210" y1="263" x2="551" y2="403" stroke="var(--paper)" stroke-width="4"/>
  </svg>

  <p class="intro intro--top">Lorem ipsum dolor sit amet,<br>consectetuer adipiscing elit,</p>

  <div class="brand">
    <span class="brand__dot"></span>
    <span class="brand__text">
      <span class="brand__name">CORVANE</span>
      <span class="brand__tagline">SEALS·GASKETS·HOSES</span>
    </span>
  </div>

  <p class="intro intro--panel">Lorem ipsum dolor sit amet,<br>consectetuer adipiscing elit,</p>

  <article class="feature feature--a">
    <svg class="feature__icon" viewBox="0 0 22 22" fill="none" stroke="var(--orange)" stroke-width="1.3">
      <polygon points="11,2 19,6.5 19,15.5 11,20 3,15.5 3,6.5"/>
      <polyline points="3,6.5 11,11 19,6.5"/><line x1="11" y1="11" x2="11" y2="20"/>
    </svg>
    <h2 class="feature__title">Lorem ipsum dolor sit amet, consectetuer</h2>
    <p class="feature__body">elit, sed diam nonummy nibh euismod tincidunt ut laoreet dolore magna aliquam erat volutpat. Ut wisi enim ad minim veniam, quis nostrud exerci tation ullamcorper suscipit lobortis nisl ut aliquip</p>
  </article>

  <article class="feature feature--b">
    <svg class="feature__icon" viewBox="0 0 22 22" fill="none" stroke="var(--orange)" stroke-width="1.3">
      <rect x="4" y="8" width="9" height="11" rx="2"/>
      <path d="M13 11h4a2 2 0 0 1 0 4h-4"/><line x1="8" y1="3" x2="8" y2="8"/>
    </svg>
    <h2 class="feature__title">Lorem ipsum dolor sit amet, consectetuer</h2>
    <p class="feature__body">elit, sed diam nonummy nibh euismod tincidunt ut laoreet dolore magna aliquam erat volutpat. Ut wisi enim ad minim veniam, quis nostrud exerci tation ullamcorper suscipit lobortis nisl ut aliquip</p>
  </article>

  <article class="feature feature--c">
    <svg class="feature__icon" viewBox="0 0 22 22" fill="none" stroke="var(--orange)" stroke-width="1.3">
      <polygon points="3,10 11,7 19,10 11,13"/>
      <polyline points="3,10 3,17 11,20 19,17 19,10"/><line x1="11" y1="13" x2="11" y2="20"/>
      <line x1="11" y1="1" x2="11" y2="4"/><line x1="5" y1="2" x2="7" y2="5"/><line x1="17" y1="2" x2="15" y2="5"/>
    </svg>
    <h2 class="feature__title">Lorem ipsum dolor sit amet, consectetuer</h2>
    <p class="feature__body">elit, sed diam nonummy nibh euismod tincidunt ut laoreet dolore magna aliquam erat volutpat. Ut wisi enim ad minim veniam, quis nostrud exerci tation ullamcorper suscipit lobortis nisl ut aliquip</p>
  </article>

  <article class="feature feature--d">
    <svg class="feature__icon" viewBox="0 0 22 22" fill="none" stroke="var(--orange)" stroke-width="1.3">
      <circle cx="11" cy="11" r="6"/>
      <path d="M11 2v3M11 17v3M2 11h3M17 11h3M4.6 4.6l2.1 2.1M15.3 15.3l2.1 2.1M4.6 17.4l2.1-2.1M15.3 6.7l2.1-2.1"/>
      <polyline points="8.5,11 10.5,13 14,9"/>
    </svg>
    <h2 class="feature__title">Lorem ipsum dolor sit amet, consectetuer</h2>
    <p class="feature__body">elit, sed diam nonummy nibh euismod tincidunt ut laoreet dolore magna aliquam erat volutpat. Ut wisi enim ad minim veniam, quis nostrud exerci tation ullamcorper suscipit lobortis nisl ut aliquip</p>
  </article>

  <article class="feature feature--e">
    <svg class="feature__icon" viewBox="0 0 22 22" fill="none" stroke="var(--orange)" stroke-width="1.3">
      <rect x="2" y="6" width="18" height="14"/>
      <line x1="6" y1="18" x2="6" y2="14"/><line x1="10" y1="18" x2="10" y2="12"/><line x1="14" y1="18" x2="14" y2="10"/>
      <polyline points="5,11 10,7 13,9 19,3"/>
    </svg>
    <h2 class="feature__title">Lorem ipsum dolor sit amet, consectetuer</h2>
    <p class="feature__body">elit, sed diam nonummy nibh euismod tincidunt ut laoreet dolore magna aliquam erat volutpat. Ut wisi enim ad minim veniam, quis nostrud exerci tation ullamcorper suscipit lobortis nisl ut aliquip</p>
  </article>

  <footer class="contact-bar">
    <span class="phone">+000 000 000</span>
    <span class="web">www.corvaneseals.com</span>
    <span class="mail">info@corvaneseals.com</span>
  </footer>
</section>

</body>
</html>
```